DL size Flyer

Design for DL Flyer double sided. One side for blocked drains and pipe relining.
Other side for general plumbing. eg leaking taps, leaking toilets, burst pipes, cctv inspections, gas installations, blocked drains.
Your local plumbing experts.
Relining pictures similar to what we need designed.

Phone number is 0478 312 564 ( on both sides)
Logo for payment methods: cash, zolt, cheque. ( on both sides)

Plumbing

```html
<!DOCTYPE html>
<html lang="en">
<head>
<meta charset="utf-8">
<title>Hillcrest Plumbing &amp; Drainage – DL Flyers</title>
<link href="https://fonts.googleapis.com/css2?family=Archivo:wght@700;800&family=PT+Sans:ital,wght@0,400;0,700;1,400;1,700&display=swap" rel="stylesheet">
<style>
  :root {
    --bg: #e9e7e4;
    --paper: #ffffff;
    --paper-grey: #f1f1f1;
    --red: #ec1c2e;
    --blue: #1d8fd6;
    --blue-deep: #0b5fa3;
    --blue-light: #1fa3e4;
    --ink: #333333;
    --phone: #1a6fb5;
    --cash: #5a9a3a;
    --cheque: #8a8580;
    --photo-green: #6f7f48;
    --photo-earth: #7a5a3e;
    --photo-blue: #5a84bd;
    --photo-pale: #c9d2de;
  }
  * { box-sizing: border-box; margin: 0; padding: 0; }
  html, body { width: 1200px; height: 1148px; overflow: hidden; }
  body { background: var(--bg); font-family: "PT Sans", sans-serif; position: relative; }

  .flyer {
    position: absolute; top: 134px; width: 417px; height: 872px;
    background: var(--paper); box-shadow: 0 4px 12px rgba(0,0,0,.25);
    overflow: hidden;
  }
  .flyer--drains { left: 151px; }
  .flyer--general { left: 625px; }

  .brand {
    position: absolute; left: 0; width: 100%;
    display: flex; align-items: center; justify-content: center; gap: 12px;
  }
  .brand__mark { width: 34px; height: 34px; border-radius: 50%; background: var(--blue); flex: none; }
  .brand__name {
    font-family: "Archivo", sans-serif; font-weight: 800; color: var(--red);
    font-size: 25px; line-height: 1.05; letter-spacing: .5px; text-transform: uppercase;
  }
  .flyer--drains .brand { top: 0; height: 128px; }
  .flyer--general .brand { top: 298px; height: 116px; }

  .photo { position: absolute; left: 0; width: 100%; }
  .photo--roots {
    top: 128px; height: 336px;
    background: linear-gradient(180deg, var(--photo-green) 0%, var(--photo-earth) 100%);
  }
  .photo--plumber {
    top: 0; height: 298px;
    background: linear-gradient(180deg, var(--photo-pale) 0%, var(--photo-blue) 100%);
  }

  .band-red {
    position: absolute; left: 0; width: 100%; background: var(--red); color: #fff;
    font-family: "Archivo", sans-serif; font-weight: 800; text-align: center; text-transform: uppercase;
  }
  .band-blue {
    position: absolute; left: 0; width: 100%; color: #fff; text-align: center;
    background: linear-gradient(90deg, var(--blue-light) 0%, var(--blue) 55%, var(--blue-deep) 100%);
  }

  .flyer--drains .band-red {
    top: 471px; height: 122px; font-size: 30px; line-height: 37px; padding-top: 24px; letter-spacing: .5px;
  }
  .flyer--drains .band-blue { top: 600px; height: 124px; padding-top: 20px; }
  .band-blue__lead { font-style: italic; font-size: 20px; line-height: 25px; }
  .band-blue__tag {
    font-family: "Archivo", sans-serif; font-weight: 700; font-size: 21px; margin-top: 8px; letter-spacing: .3px;
  }

  .flyer--general .band-red { top: 414px; height: 249px; padding-top: 20px; }
  .band-red__title { font-size: 28px; line-height: 36px; letter-spacing: .5px; }
  .services {
    list-style: none; display: grid; grid-template-columns: 172px 190px;
    column-gap: 14px; row-gap: 12px; margin: 20px 0 0 22px; text-align: left;
    font-family: "PT Sans", sans-serif; font-weight: 700; text-transform: none; font-size: 20px;
  }
  .services li { display: flex; align-items: center; gap: 6px; white-space: nowrap; }
  .services svg { width: 17px; height: 17px; flex: none; }

  .flyer--general .band-blue { top: 669px; height: 57px; padding-top: 5px; }
  .band-blue__note { font-style: italic; font-weight: 700; font-size: 16px; line-height: 22px; }

  .footer { position: absolute; left: 0; bottom: 0; width: 100%; height: 140px; }
  .flyer--general .footer { background: var(--paper-grey); }
  .footer__row { display: flex; align-items: center; gap: 5px; margin: 24px 0 0 18px; }
  .pay {
    width: 38px; height: 38px; border-radius: 6px; display: flex; align-items: center; justify-content: center;
    font-family: "PT Sans", sans-serif; font-weight: 700; font-size: 10px; color: #fff;
    box-shadow: 0 1px 2px rgba(0,0,0,.3);
  }
  .pay--cash { background: var(--cash); font-size: 11px; }
  .pay--cheque { background: var(--cheque); font-size: 9px; }
  .pay--zolt { background: #fff; color: var(--phone); border: 1px solid #ccc; }
  .phone {
    display: flex; align-items: center; gap: 8px; margin-left: 16px;
    font-family: "Archivo", sans-serif; font-weight: 700; font-size: 27px; color: var(--phone); letter-spacing: .5px;
  }
  .phone svg { width: 20px; height: 20px; }
  .address { text-align: center; font-size: 13.5px; color: var(--ink); margin-top: 14px; }
</style>
</head>
<body>

<article class="flyer flyer--drains">
  <header class="brand">
    <span class="brand__mark"></span>
    <span class="brand__name">Hillcrest<br>Plumbing &amp; Drainage</span>
  </header>
  <div class="photo photo--roots" role="img" aria-label="Photo: house with lawn and a cutaway of tree roots breaking into an underground drain pipe"></div>
  <h2 class="band-red">Blocked drains &amp;<br>pipe relining</h2>
  <div class="band-blue">
    <p class="band-blue__lead">A fast, clean, permanent solution<br>for fixing blocked drains.</p>
    <p class="band-blue__tag">Your local plumbing experts.</p>
  </div>
  <footer class="footer">
    <div class="footer__row">
      <span class="pay pay--cash">CASH</span>
      <span class="pay pay--cheque">CHEQUE</span>
      <span class="pay pay--zolt">ZOLT</span>
      <span class="phone">
        <svg viewBox="0 0 24 24"><path fill="currentColor" d="M6.6 10.8a15.1 15.1 0 0 0 6.6 6.6l2.2-2.2a1 1 0 0 1 1-.25 11.4 11.4 0 0 0 3.6.57 1 1 0 0 1 1 1V20a1 1 0 0 1-1 1A17 17 0 0 1 3 4a1 1 0 0 1 1-1h3.5a1 1 0 0 1 1 1c0 1.25.2 2.45.57 3.6a1 1 0 0 1-.25 1z"/></svg>
        0478 312 564
      </span>
    </div>
    <p class="address">14 Fern Street, 2155 Sydney - Kellyville New South Wales</p>
  </footer>
</article>

<article class="flyer flyer--general">
  <div class="photo photo--plumber" role="img" aria-label="Photo: plumber in blue work clothes repairing pipes under a sink with a wrench"></div>
  <header class="brand">
    <span class="brand__mark"></span>
    <span class="brand__name">Hillcrest<br>Plumbing &amp; Drainage</span>
  </header>
  <section class="band-red">
    <h2 class="band-red__title">Your local<br>plumbing experts</h2>
    <ul class="services">
      <li><svg viewBox="0 0 20 20"><circle cx="10" cy="10" r="8" fill="none" stroke="#fff" stroke-width="1.8"/><path d="M6 10.3l2.7 2.6L14 7.5" fill="none" stroke="#fff" stroke-width="1.8"/></svg>Leaking taps</li>
      <li><svg viewBox="0 0 20 20"><circle cx="10" cy="10" r="8" fill="none" stroke="#fff" stroke-width="1.8"/><path d="M6 10.3l2.7 2.6L14 7.5" fill="none" stroke="#fff" stroke-width="1.8"/></svg>CCTV inspections</li>
      <li><svg viewBox="0 0 20 20"><circle cx="10" cy="10" r="8" fill="none" stroke="#fff" stroke-width="1.8"/><path d="M6 10.3l2.7 2.6L14 7.5" fill="none" stroke="#fff" stroke-width="1.8"/></svg>Leaking toilets</li>
      <li><svg viewBox="0 0 20 20"><circle cx="10" cy="10" r="8" fill="none" stroke="#fff" stroke-width="1.8"/><path d="M6 10.3l2.7 2.6L14 7.5" fill="none" stroke="#fff" stroke-width="1.8"/></svg>Gas installations</li>
      <li><svg viewBox="0 0 20 20"><circle cx="10" cy="10" r="8" fill="none" stroke="#fff" stroke-width="1.8"/><path d="M6 10.3l2.7 2.6L14 7.5" fill="none" stroke="#fff" stroke-width="1.8"/></svg>Burst pipes</li>
      <li><svg viewBox="0 0 20 20"><circle cx="10" cy="10" r="8" fill="none" stroke="#fff" stroke-width="1.8"/><path d="M6 10.3l2.7 2.6L14 7.5" fill="none" stroke="#fff" stroke-width="1.8"/></svg>Blocked drains</li>
    </ul>
  </section>
  <div class="band-blue">
    <p class="band-blue__note">Provides a solution to the whole problem,<br>not just temporary relief from the symptoms.</p>
  </div>
  <footer class="footer">
    <div class="footer__row">
      <span class="pay pay--cash">CASH</span>
      <span class="pay pay--cheque">CHEQUE</span>
      <span class="pay pay--zolt">ZOLT</span>
      <span class="phone">
        <svg viewBox="0 0 24 24"><path fill="currentColor" d="M6.6 10.8a15.1 15.1 0 0 0 6.6 6.6l2.2-2.2a1 1 0 0 1 1-.25 11.4 11.4 0 0 0 3.6.57 1 1 0 0 1 1 1V20a1 1 0 0 1-1 1A17 17 0 0 1 3 4a1 1 0 0 1 1-1h3.5a1 1 0 0 1 1 1c0 1.25.2 2.45.57 3.6a1 1 0 0 1-.25 1z"/></svg>
        0478 312 564
      </span>
    </div>
    <p class="address">14 Fern Street, 2155 Sydney - Kellyville New South Wales</p>
  </footer>
</article>

</body>
</html>
```